Movies and Cinema preview and Review Site

I'm looking for a well designed movies and cinema preview and review website which i would talk about new movies which are yet to be released to the public, upcoming movies, movies which are currently been shown on the cinema and others. Categories will include - thriller movies, Action movies, Best seller, Adventures, family, comedy. By the left hand widget of the website will feature upcoming block buster movies while the right hand side on the website review of released movies. At the center will be news of upcoming movies. My target is primarily Americans and would be dealing strictly on America movies. I require glossy images on my website. My website name - amber quill.

```html
<!DOCTYPE html>
<html lang="en">
<head>
<meta charset="utf-8">
<title>Amber Quill – Hollow Star Review</title>
<link href="https://fonts.googleapis.com/css2?family=Titillium+Web:wght@400;700&family=Open+Sans:wght@400;600;700&family=Merriweather:wght@400;700&display=swap" rel="stylesheet">
<style>
:root{
  --board:#4b3a38;
  --board-sub:#e7dede;
  --board-muted:#8c7f7d;
  --page:#ffffff;
  --red:#a81500;
  --red-dark:#8c1100;
  --footer:#dc3232;
  --logo:#9be33c;
  --ink:#222222;
  --body:#444444;
  --muted:#999999;
  --line:#e4e4e4;
  --gold:#f2c200;
  --pink:#e8435a;
  --pink-dark:#c8304a;
  --navy:#2f3a4a;
  --navy-text:#c9d2de;
}
*{box-sizing:border-box;margin:0;padding:0}
html,body{width:1200px;height:3000px;overflow:hidden}
body{background:var(--board);font-family:"Open Sans",Arial,sans-serif;color:var(--body);position:relative}
.abs{position:absolute}

.board-title{left:0;width:1200px;top:30px;text-align:center;font-family:"Titillium Web",Arial,sans-serif;font-weight:700;font-size:38px;color:#fff}
.board-sub{left:0;width:1200px;top:134px;text-align:center;font-family:"Titillium Web",Arial,sans-serif;font-weight:700;font-size:30px;color:var(--board-sub);text-decoration:underline}
.board-note{left:200px;width:1000px;top:196px;text-align:center;font-family:"Titillium Web",Arial,sans-serif;font-weight:700;font-size:29px;color:var(--board-muted)}

.page{left:62px;top:348px;width:1068px;height:2392px;background:var(--page)}
.topbar{left:62px;top:348px;width:1068px;height:44px;border-bottom:1px solid var(--line);font-size:12px;color:#777;display:flex;align-items:center}
.topbar .home{width:44px;height:44px;border-right:1px solid var(--line);display:flex;align-items:center;justify-content:center}
.ticker{padding-left:18px;white-space:nowrap;overflow:hidden;width:840px}
.ticker span{margin-right:22px}
.social{display:flex;margin-left:auto;height:44px}
.social i{width:34px;height:44px;border-left:1px solid var(--line);display:flex;align-items:center;justify-content:center}
.social i b{width:10px;height:10px;background:#888;border-radius:2px;display:block}

.navbar{left:62px;top:392px;width:1068px;height:46px;background:var(--red)}
.logo{left:108px;top:400px;display:flex;align-items:center;gap:8px;font-family:"Open Sans",Arial,sans-serif;font-weight:700;font-size:22px;color:var(--logo)}
.logo i{width:20px;height:20px;background:var(--logo);display:block}
.nav{left:780px;top:392px;height:46px;display:flex}
.nav a{color:#fff;text-decoration:none;font-size:13px;font-weight:600;padding:0 20px;line-height:46px}
.nav a.active{background:var(--red-dark)}

.crumbs{left:108px;top:464px;width:668px;font-size:11px;font-weight:700;color:#222;padding-bottom:8px;border-bottom:1px solid var(--line);letter-spacing:.3px}
.crumbs span{margin:0 14px;color:#888}
.crumbs em{font-style:normal;color:#888;font-weight:600}
.post-title{left:108px;top:500px;font-family:"Merriweather",Georgia,serif;font-weight:700;font-size:31px;color:var(--ink)}
.meta{left:108px;top:550px;font-size:11.5px;color:#777}
.meta a{color:var(--red);font-weight:700;text-decoration:none}

.copy{left:108px;width:668px;font-size:12.2px;line-height:20px;color:var(--body)}
.copy p{margin-bottom:14px}
.hero{left:176px;top:758px;width:532px;height:300px;background:linear-gradient(135deg,#2a2a28 0%,#4a4038 45%,#6b5a4a 70%,#1d1d1b 100%)}

.review{left:108px;top:1288px;width:668px;height:350px;background:var(--red);border:1px solid #7a0f00;color:#fff;padding:14px 12px}
.review h3{font-size:15px;font-weight:700;margin-bottom:10px}
.crit{display:flex;align-items:center;justify-content:space-between;height:36px;border-top:1px solid rgba(255,255,255,.25);font-size:12.5px}
.summary{position:absolute;left:12px;top:200px;width:540px;font-size:12.2px;line-height:19px}
.summary b{display:block;font-size:12px}
.score{position:absolute;right:14px;top:196px}

.shares{left:108px;top:1664px;display:flex;gap:28px}
.shares span{font-size:10px;color:#fff;padding:2px 8px;border-radius:2px;font-weight:600}
.sec-head{left:108px;width:668px;font-family:"Merriweather",Georgia,serif;font-weight:700;font-size:13px;color:var(--ink);padding-bottom:8px;border-bottom:1px solid var(--line)}
.sec-head::after{content:"";position:absolute;left:0;bottom:-1px;width:40px;height:2px;background:var(--ink)}
.avatar{left:108px;top:1758px;width:84px;height:84px;border-radius:50%;background:linear-gradient(160deg,#6a87b0,#3c4c72)}
.author{left:208px;top:1758px;font-family:"Merriweather",Georgia,serif;font-weight:700;font-size:17px;color:var(--ink)}

.thumb{top:1924px;width:148px;height:148px}
.tag{position:absolute;right:4px;top:4px;background:var(--red);color:#fff;font-size:11px;padding:2px 6px}
.rel-title{font-size:13px;color:#333;top:2088px}
.rel-by{font-size:10.5px;color:#777;top:2114px}
.rel-by b{color:var(--red)}

.reply-head{left:108px;top:2166px;font-family:"Merriweather",Georgia,serif;font-weight:700;font-size:16px;color:var(--ink)}
.reply-head::after{content:"";position:absolute;left:0;top:30px;width:40px;height:2px;background:var(--ink)}
.field{left:108px;border:1px solid #ddd;font-size:11px;color:#999;padding:6px 12px}
.btn{left:108px;top:2514px;width:120px;height:28px;background:var(--red);color:#fff;font-size:11.5px;font-weight:700;display:flex;align-items:center;justify-content:center}

.footer{left:62px;top:2576px;width:1068px;height:164px;background:var(--footer)}
.footer-logo{left:108px;top:2620px;display:flex;align-items:center;gap:8px;font-weight:700;font-size:22px;color:var(--logo)}
.footer-logo i{width:20px;height:20px;background:var(--logo);display:block}
.footer-copy{left:108px;top:2704px;font-size:11px;color:#5a1010}

.widget-bar{left:834px;top:462px;width:248px;height:28px;background:var(--red);color:#fff;font-size:11px;font-weight:700;display:flex;align-items:center;justify-content:center}
.rv{left:834px;width:248px;height:88px;border-bottom:1px solid var(--line)}
.rv .pic{position:absolute;left:0;top:20px;width:48px;height:48px;border-radius:50%}
.rv .name{position:absolute;left:66px;top:16px;font-size:12px;color:#333;width:170px}
.rv .rate{position:absolute;left:66px;top:46px;font-size:11px;color:#999}
.rv .date{position:absolute;right:0;top:46px;font-size:11px;color:#999;font-weight:600}
.search-label{left:834px;top:1140px;width:248px;font-size:11px;font-weight:700;color:#222;padding-bottom:8px;border-bottom:1px solid var(--line)}
.search{left:834px;top:1188px;width:248px;height:32px;border:1px solid #ddd;font-size:11px;color:#999;display:flex;align-items:center;gap:8px;padding-left:12px}
.tabs{left:834px;top:1242px;width:248px;height:558px;background:var(--navy)}
.tabs-top{left:834px;top:1242px;width:248px;height:50px;background:var(--pink)}
.tab{top:1254px;height:30px;font-size:11px;display:flex;align-items:center;justify-content:center}
.tab.on{left:846px;width:74px;background:#fff;color:var(--pink)}
.tab.off{left:922px;width:74px;background:var(--pink-dark);color:#fff}
.li{left:846px;width:226px}
.li .pic{position:absolute;left:0;top:0;width:52px;height:52px;border-radius:50%}
.li .t{position:absolute;left:70px;top:-2px;font-size:12.2px;line-height:19px;color:var(--navy-text)}
.li .d{position:absolute;left:70px;font-size:8.5px;color:#7d8898}
.pager{left:834px;top:1764px;width:248px;text-align:center;font-size:11px;color:var(--navy-text)}
</style>
</head>
<body>
<svg width="0" height="0" class="abs" aria-hidden="true">
  <defs>
    <polygon id="star" points="6,0 7.8,4 12,4.4 8.8,7.2 9.8,11.6 6,9.3 2.2,11.6 3.2,7.2 0,4.4 4.2,4"/>
  </defs>
</svg>

<h1 class="abs board-title">WEBSITE DESIGN IDEA - 1d (Functionality)</h1>
<p class="abs board-sub">Circle Style Review System (placed at bottom)</p>
<p class="abs board-note">Review can be placed either on Top, In Between or Bottom</p>

<div class="abs page"></div>

<div class="abs topbar">
  <div class="home"><svg width="12" height="12" viewBox="0 0 12 12"><path d="M1 6 6 1l5 5H9.5v5h-2.5V8H5v3H2.5V6z" fill="#888"/></svg></div>
  <div class="ticker"><span>First Trailer!</span><span>Wand Keeper Update: 18 Years Ago, World Got Its First Mira, Theo And Finn [Watch]</span><span>The Porcelain Saints Premiere Date And Official Trai</span></div>
  <div class="social"><i><b></b></i><i><b></b></i><i><b></b></i><i><b></b></i></div>
</div>

<div class="abs navbar"></div>
<div class="abs logo"><i></i>Amber Quill</div>
<nav class="abs nav"><a class="active">Home</a><a>News</a><a>Reviews</a><a>Contact Us</a></nav>

<div class="abs crumbs">HOME<span>›</span>REVIEWS<span>›</span>COMEDY MOVIES<span>›</span><em>Hollow Star Review</em></div>
<h2 class="abs post-title">Hollow Star Review</h2>
<div class="abs meta">by <a>Dana Reyes</a> / 29th August 2016 / <a>Comedy Movies</a>, <a>Drama</a> / <a>No Comments</a></div>

<div class="abs copy" style="top:586px">
  <p>Sometimes you’ve just to hold up your hands and admit you don’t have the first idea what’s going on. But, in the case of Aleksy Korvan’s surreal adaptation of Tomas Brenik’s cult 1965 novel, that’s no bad thing, as his swan song is designed to puzzle and provoke rather than provide precise meaning.</p>
  <p>Returning to film-making after a 15-year hiatus, Korvan seemed determined to pay homage to his cinematic and literary influences, while also demonstrating that he could be simultaneously intellectual and playful. He succeeds in proving that reality is in the eye of the beholder. But even the shrewdest cinéaste will need to concentrate to catch all the insights into the arbitrary nature of language, the elusiveness of freedom and the difficulty of imposing order upon chaos.</p>
</div>

<div class="abs hero" role="img" aria-label="Film still: a man and a woman in a dim room, warm shadows"></div>

<div class="abs copy" style="top:1078px">
  <p>There is no story to speak of. Instead, Korvan billets failing law student Julien Marot at the guest house run by Celine Arnaud and the gobbledegook-spouting Henri Lavelle and lets him lose his mind, as he becomes obsessed with finding links between a hanged sparrow, a yonic water stain, an arrow carved into the ceiling and the lips of Arnaud’s newlywed daughter (Lia Serrano) and her disfigured maid/niece (Noemie Vidal). Add into the mix a fellow guest who keeps getting beaten up on his nocturnal jaunts, a priest with a secret stash of bees and a lookalike whose husband resembles Pip Harlow and you get the gist.</p>
  <p>Strikingly designed by Petra Solan and photographed by Marek Ostrow, this ‘metaphysical noir thriller’ delights in its quirky characters, odd occurrences and strange symbolism, whose significance remains shrouded in ambiguity. But Korvan also challenges the audience to demand more out of cinema than escapist entertainment.</p>
</div>

<section class="abs review">
  <h3>Hollow Star Review</h3>
  <div class="crit">Story - 78<svg width="28" height="28"><circle cx="14" cy="14" r="10" fill="none" stroke="var(--gold)" stroke-width="3"/></svg></div>
  <div class="crit">Comedy - 55<svg width="28" height="28"><circle cx="14" cy="14" r="10" fill="none" stroke="var(--gold)" stroke-width="3"/></svg></div>
  <div class="crit">Direction - 67<svg width="28" height="28"><circle cx="14" cy="14" r="10" fill="none" stroke="var(--gold)" stroke-width="3"/></svg></div>
  <div class="crit">Screenplay - 72<svg width="28" height="28"><circle cx="14" cy="14" r="10" fill="none" stroke="var(--gold)" stroke-width="3"/></svg></div>
  <div class="summary"><b>Summary</b>Marot who has just failed the bar, and his companion Keller, who has recently quit his fashion job, are staying at a guesthouse run by the intermittently paralytic Madame Orlow. Upon discovering a sparrow hanged in the woods near the house, Marot’s reality mutates into a whirlwind of tension, histrionics, foreboding omens, and surrealistic logic as he becomes obsessed with Madame Orlow’s daughter Ana, newly married to Lucien.</div>
  <svg class="score" width="84" height="84" viewBox="0 0 84 84">
    <circle cx="42" cy="42" r="33" fill="none" stroke="#555" stroke-width="12"/>
    <circle cx="42" cy="42" r="33" fill="none" stroke="var(--gold)" stroke-width="12" stroke-dasharray="141 207" transform="rotate(-90 42 42)"/>
    <circle cx="42" cy="42" r="27" fill="#fff"/>
    <text x="42" y="49" text-anchor="middle" font-family="Open Sans, sans-serif" font-size="20" font-weight="700" fill="#b88f00">68</text>
  </svg>
</section>

<div class="abs shares">
  <span style="background:#3c9bd6">Share</span>
  <span style="background:#eee;color:#666;border:1px solid #ccc">+1 0</span>
  <span style="background:#4a66a0">Like 0</span>
  <span style="background:#eee;color:#b22;border:1px solid #ccc">Save</span>
</div>

<h4 class="abs sec-head" style="top:1706px">ABOUT THE AUTHOR</h4>
<div class="abs avatar" role="img" aria-label="Author portrait"></div>
<div class="abs author">Dana Reyes</div>

<h4 class="abs sec-head" style="top:1874px">RELATED POSTS</h4>
<div class="abs thumb" style="left:108px;background:linear-gradient(160deg,#8a6a4a,#c9b9a4 50%,#5b4a3a)" role="img" aria-label="Horses racing in a dusty arena"><span class="tag">69%</span></div>
<div class="abs thumb" style="left:282px;background:linear-gradient(180deg,#6b8fb0,#8b6a4a 55%,#3a7fb8)" role="img" aria-label="Sea otters above blue water"><span class="tag">6.9/10</span></div>
<div class="abs rel-title" style="left:108px">Chariot King Review</div>
<div class="abs rel-by" style="left:108px">by <b>Dana Reyes</b></div>
<div class="abs rel-title" style="left:282px">Reef Runners Review</div>
<div class="abs rel-by" style="left:282px">by <b>Dana Reyes</b></div>

<h4 class="abs reply-head">LEAVE A REPLY</h4>
<div class="abs field" style="top:2210px;width:668px;height:176px;padding-top:10px">Comment Text*</div>
<div class="abs field" style="top:2396px;width:250px;height:30px">Name*</div>
<div class="abs field" style="top:2432px;width:250px;height:30px">Email*</div>
<div class="abs field" style="top:2468px;width:250px;height:30px">Website</div>
<div class="abs btn">Post Comment</div>

<div class="abs widget-bar">Release Movie Reviews</div>
<div class="abs rv" style="top:492px"><div class="pic" style="background:linear-gradient(135deg,#5a4a3a,#1e1e1e)" role="img" aria-label="Film poster"></div><div class="name">Silent Meridian Review</div><div class="rate">5.7/10</div><div class="date">Aug 30, 2016</div></div>
<div class="abs rv" style="top:580px"><div class="pic" style="background:linear-gradient(135deg,#3a4a6a,#1a1a2a)" role="img" aria-label="Film poster"></div><div class="name">Iron Tide: Reckoning Review</div><svg class="abs" style="left:66px;top:46px" width="90" height="12"><use href="#star" x="0" fill="var(--gold)"/><use href="#star" x="16" fill="var(--gold)"/><use href="#star" x="32" fill="var(--gold)"/><use href="#star" x="48" fill="var(--gold)"/><use href="#star" x="64" fill="#ccc"/></svg><div class="date">Aug 30, 2016</div></div>
<div class="abs rv" style="top:668px"><div class="pic" style="background:linear-gradient(135deg,#4a5a7a,#141420)" role="img" aria-label="Film poster"></div><div class="name">Rogue Company Movie Review</div><svg class="abs" style="left:66px;top:46px" width="90" height="12"><use href="#star" x="0" fill="var(--gold)"/><use href="#star" x="16" fill="var(--gold)"/><use href="#star" x="32" fill="var(--gold)"/><use href="#star" x="48" fill="var(--gold)"/><use href="#star" x="64" fill="#ccc"/></svg><div class="date">Aug 29, 2016</div></div>
<div class="abs rv" style="top:756px"><div class="pic" style="background:linear-gradient(135deg,#4a3a30,#1a1614)" role="img" aria-label="Film poster"></div><div class="name">Hollow Star Review</div><svg class="abs" style="left:66px;top:42px" width="20" height="20"><path d="M10 2a8 8 0 1 1-8 8" fill="none" stroke="var(--gold)" stroke-width="2.5"/></svg><div class="date">Aug 29, 2016</div></div>
<div class="abs rv" style="top:844px"><div class="pic" style="background:linear-gradient(135deg,#9a7a50,#3a2a1a)" role="img" aria-label="Film poster"></div><div class="name">Chariot King Review</div><div class="rate">69%</div><div class="date">Aug 29, 2016</div></div>
<div class="abs rv" style="top:932px"><div class="pic" style="background:linear-gradient(135deg,#5a8ab0,#6a4a30)" role="img" aria-label="Film poster"></div><div class="name">Reef Runners Review</div><div class="rate">6.9/10</div><div class="date">Aug 29, 2016</div></div>
<div class="abs rv" style="top:1020px;border-bottom:none"><div class="pic" style="background:linear-gradient(135deg,#6a5a4a,#2a2a30)" role="img" aria-label="Film poster"></div><div class="name">‘Liberty Shield: House Divided’ Spoiler Review</div><svg class="abs" style="left:66px;top:50px" width="90" height="12"><use href="#star" x="0" fill="var(--gold)"/><use href="#star" x="16" fill="var(--gold)"/><use href="#star" x="32" fill="var(--gold)"/><use href="#star" x="48" fill="var(--gold)"/><use href="#star" x="64" fill="#ccc"/></svg><div class="date" style="top:50px">Aug 29, 2016</div></div>

<div class="abs search-label">SEARCH</div>
<div class="abs search"><svg width="12" height="12" viewBox="0 0 12 12"><circle cx="5" cy="5" r="3.8" fill="none" stroke="#999" stroke-width="1.4"/><path d="M8 8l3 3" stroke="#999" stroke-width="1.4"/></svg>Search the site</div>

<div class="abs tabs"></div>
<div class="abs tabs-top"></div>
<div class="abs tab on">Latest</div>
<div class="abs tab off">Popular</div>
<div class="abs li" style="top:1312px"><div class="pic" style="background:linear-gradient(135deg,#5a4a3a,#1e1e1e)" role="img" aria-label="Film thumbnail"></div><div class="t">Silent Meridian Review</div><div class="d" style="top:22px">AUG 30, 2016 • NO COMMENT</div></div>
<div class="abs li" style="top:1390px"><div class="pic" style="background:linear-gradient(135deg,#3a4a6a,#1a1a2a)" role="img" aria-label="Film thumbnail"></div><div class="t">Iron Tide: Reckoning Review</div><div class="d" style="top:22px">AUG 30, 2016 • NO COMMENT</div></div>
<div class="abs li" style="top:1470px"><div class="pic" style="background:linear-gradient(135deg,#6a3a2a,#151515)" role="img" aria-label="Film thumbnail"></div><div class="t">Hive Protocol The Final Chapter: Check Out The First Trailer!</div><div class="d" style="top:62px">AUG 30, 2016 • NO COMMENT</div></div>
<div class="abs li" style="top:1566px"><div class="pic" style="background:linear-gradient(135deg,#7a5a3a,#222)" role="img" aria-label="Film thumbnail"></div><div class="t">Wand Keeper Update: 16 Years Ago, World Got Its First...</div><div class="d" style="top:62px">AUG 30, 2016 • NO COMMENT</div></div>
<div class="abs li" style="top:1664px"><div class="pic" style="background:linear-gradient(135deg,#3a3030,#0e0e0e)" role="img" aria-label="Film thumbnail"></div><div class="t">The Porcelain Saints Premiere Date And Official Trailer Released!</div><div class="d" style="top:62px">AUG 30, 2016 • NO COMMENT</div></div>
<div class="abs pager">4 &nbsp;&nbsp;&nbsp; NEXT ›</div>

<div class="abs footer"></div>
<div class="abs footer-logo"><i></i>Amber Quill</div>
<div class="abs footer-copy">Amber Quill Copyright © 2016</div>
</body>
</html>
```